https://dorvakel.com

We need a cool technology design for our Managed IT Services company. We are located in Coral Springs Florida. We provide all IT services and support for small to medium sized businesses. We would like to see designs that use our blue and white colors from our website.

```html
<!DOCTYPE html>
<html lang="en">
<head>
<meta charset="utf-8">
<title>Dorvakel business card</title>
<link rel="stylesheet" href="https://fonts.googleapis.com/css2?family=Montserrat:wght@600&family=Arimo:wght@400;700&display=swap">
<style>
  :root {
    --navy: #0f2d5c;
    --navy-deep: #0b2350;
    --paper: #f4f5f6;
    --arc-grey: #9a9ea3;
    --ink-light: #dfe5ee;
    --stage: #2a2a2a;
  }
  * { margin: 0; padding: 0; box-sizing: border-box; }
  html, body { width: 1200px; height: 997px; overflow: hidden; background: var(--stage); }
  .canvas { position: relative; width: 1200px; height: 997px; }

  .card { position: absolute; width: 520px; height: 300px; overflow: hidden; }

  .card-front {
    left: 70px; top: 150px;
    background: linear-gradient(160deg, #173a70, var(--navy-deep));
    display: flex; align-items: center; justify-content: center;
  }
  .front-name {
    font-family: "Montserrat", sans-serif; font-weight: 600;
    font-size: 64px; letter-spacing: 1px; color: #ffffff;
  }

  .card-back { left: 610px; top: 480px; background: var(--paper); }
  .card-back svg { position: absolute; inset: 0; }

  .back-name {
    position: absolute; left: 40px; top: 118px;
    font-family: "Montserrat", sans-serif; font-weight: 600;
    font-size: 36px; color: var(--navy); letter-spacing: 0.5px;
  }

  .contact {
    position: absolute; right: 26px; top: 32px; text-align: right;
    font-family: "Arimo", sans-serif; color: var(--ink-light);
    font-size: 12px; line-height: 1.35;
  }
  .contact .person { font-weight: 700; font-size: 15px; color: #ffffff; letter-spacing: 0.5px; }
  .contact .role { margin-bottom: 14px; }
  .contact .address { margin-bottom: 14px; }
  .contact .line { display: flex; justify-content: flex-end; align-items: center; gap: 6px; height: 18px; }
  .contact .icon { width: 12px; height: 12px; }
  .contact .web { font-weight: 700; color: #ffffff; margin-top: 12px; font-size: 12.5px; }
</style>
</head>
<body>
<main class="canvas">

  <section class="card card-front" aria-label="Card front">
    <span class="front-name">DORVAKEL</span>
  </section>

  <section class="card card-back" aria-label="Card back">
    <svg width="520" height="300" viewBox="0 0 520 300" aria-hidden="true">
      <path class="navy-field" d="M360,0 C290,70 305,215 470,300 L520,300 L520,0 Z" fill="var(--navy)"/>
      <path class="divider-arc" d="M340,18 C292,95 312,215 445,292" fill="none" stroke="var(--arc-grey)" stroke-width="6" stroke-linecap="round"/>
    </svg>

    <span class="back-name">DORVAKEL</span>

    <div class="contact">
      <div class="person">MARTA ELSWICK</div>
      <div class="role">Director of Sales &amp; Marketing</div>
      <div class="address">27 harbor lane, suite 4<br>Coral Springs, USA.</div>
      <div class="line">555 310 2846
        <svg class="icon" viewBox="0 0 12 12"><circle cx="6" cy="6" r="6" fill="#c9d0da"/><path d="M3.5,4 L4.5,3 L5.5,4.5 L4.8,5.2 Q5.6,6.6 6.8,7.2 L7.5,6.5 L9,7.5 L8,8.5 Q5,8.5 3.5,4Z" fill="var(--navy)"/></svg>
      </div>
      <div class="line">555 310 2907
        <svg class="icon" viewBox="0 0 12 12"><circle cx="6" cy="6" r="6" fill="#c9d0da"/><rect x="4.2" y="2.8" width="3.6" height="6.4" rx="0.6" fill="var(--navy)"/></svg>
      </div>
      <div class="line">555 310 2950
        <svg class="icon" viewBox="0 0 12 12"><circle cx="6" cy="6" r="6" fill="#c9d0da"/><rect x="3" y="4" width="6" height="4" fill="var(--navy)"/></svg>
      </div>
      <div class="line">marta@dorvakel.com</div>
      <div class="web">www.dorvakel.com</div>
    </div>
  </section>

</main>
</body>
</html>
```